6"x9" Postcard Mailer

A 6"x9" Postcard mailer targeted to forensic laboratories to advertise or mock forensic samples (https://veltrasync.example/products/mock-forensic-samples/).

Here is some copy, but we can modify if there is not enough space:

Headline:
Expedite Training, Validation, & R&D with Our Ready-to-Use Mock Samples

Bullet Points:

- Wide Variety of Sample Types: IRB-approved samples mimicking crime scene substances, including semen, hair, bone, saliva, blood, and vaginal epithelial cells.
- Diverse Scenarios: Simulate sexual assault and degraded samples for varied conditions.
- Custom Solutions: Tailored DNA quantities and concentrations to suit your lab's needs.

Use discount code PRAX47 for a 10% discount

```html
<!DOCTYPE html>
<html lang="en">
<head>
<meta charset="utf-8">
<title>VeltraSync Postcard Mailer</title>
<link rel="stylesheet" href="https://fonts.googleapis.com/css2?family=Gelasio:wght@400;600;700&display=swap">
<style>
  :root{
    --stage:#545253;
    --navy:#0a1230;
    --brand-blue:#1f4f9c;
    --code-blue:#2488d4;
    --ink:#1d1d22;
    --paper:#ececec;
    --white:#ffffff;
  }
  *{box-sizing:border-box;margin:0;padding:0}
  html,body{width:1200px;height:1200px;overflow:hidden}
  body{background:var(--stage);font-family:"Gelasio",Georgia,serif;position:relative}
  .card{position:absolute;left:246px;width:708px;height:477px;overflow:hidden}
  .card-front{top:81px;color:var(--white)}
  .card-back{top:614px;background:var(--paper);color:var(--ink)}
  .photo{position:absolute;inset:0;
    background:radial-gradient(ellipse at 55% 45%,#2f5fe0 0%,#1838a8 35%,#0b1850 65%,#050814 100%),var(--navy)}
  .photo::after{content:"";position:absolute;inset:0;
    background:linear-gradient(to bottom,rgba(0,0,0,0) 55%,rgba(26,80,240,.85) 100%)}
  .frame{position:absolute;left:18px;top:17px;right:17px;bottom:17px;border:1.5px solid var(--white)}
  .brand-name{position:absolute;left:0;right:0;text-align:center;font-weight:400;line-height:1}
  .card-front .brand-name{top:42px;font-size:64px}
  .slogan{position:absolute;font-size:20px;letter-spacing:6px;font-weight:600;white-space:nowrap}
  .card-front .slogan{left:0;right:0;top:112px;text-align:center}
  .headline{position:absolute;left:0;right:0;top:214px;text-align:center;font-size:27px;line-height:34px;font-weight:400}
  .front-contact{position:absolute;left:0;right:0;top:420px;text-align:center;font-size:21px}
  .front-contact svg{vertical-align:-3px;margin-right:3px}
  .divider{margin:0 8px}
  .dna-art{position:absolute;inset:0;
    background:radial-gradient(ellipse at 80% 50%,rgba(160,200,235,.7) 0%,rgba(200,222,240,.4) 35%,rgba(236,236,236,0) 70%),var(--paper)}
  .features{position:absolute;left:30px;top:26px;width:468px;list-style:none}
  .feature{position:relative;padding-left:25px;font-size:21.5px;line-height:26.5px;text-align:justify;margin-bottom:15px}
  .feature svg{position:absolute;left:0;top:5px}
  .feature-title{color:var(--brand-blue);display:block;margin-bottom:4px}
  .offer{position:absolute;left:528px;top:17px;width:152px;height:208px;background:var(--brand-blue);padding:5px}
  .offer-inner{border:1px dashed #b9c9e6;height:100%;text-align:center;color:var(--white)}
  .offer-pct{font-size:58px;font-weight:700;line-height:54px;padding-top:10px;letter-spacing:-2px}
  .offer-off{font-size:52px;font-weight:700;line-height:50px}
  .offer-label{font-size:10.5px;font-weight:600;margin-top:20px}
  .offer-code{margin:6px 10px 0;background:var(--code-blue);font-size:24px;font-weight:700;line-height:36px}
  .card-back .brand-name{left:32px;right:auto;top:285px;font-size:62px;color:var(--brand-blue);text-align:left}
  .card-back .slogan{left:38px;top:358px;color:var(--brand-blue);font-weight:400;letter-spacing:6px}
  .back-contact{position:absolute;left:35px;font-size:24px;display:flex;align-items:center;gap:8px;white-space:nowrap}
  .back-phone{top:393px}
  .back-web{top:424px}
  .web-name{color:var(--brand-blue)}
  .mail-area{position:absolute;background:var(--white)}
  .mail-area-top{left:566px;top:250px;width:142px;height:227px}
  .mail-area-bottom{left:376px;top:419px;width:332px;height:58px}
</style>
</head>
<body>

<section class="card card-front">
  <div class="photo" role="img" aria-label="Photo of gloved hands swabbing a blood stain with a forensic swab"></div>
  <div class="frame"></div>
  <h1 class="brand-name">VeltraSync</h1>
  <p class="slogan">PRECISION IN EVERY SAMPLE</p>
  <h2 class="headline">Expedite Training, Validation, &amp; R&amp;D<br>with Our Ready-to-Use Mock Samples</h2>
  <p class="front-contact">
    <svg width="18" height="18" viewBox="0 0 24 24" fill="none" stroke="#fff" stroke-width="1.6"><path d="M5 3h4l2 5-2.5 1.5a11 11 0 0 0 6 6L16 13l5 2v4a2 2 0 0 1-2 2A16 16 0 0 1 3 5a2 2 0 0 1 2-2z"/></svg>+1 555 014 2876<span class="divider">|</span><svg width="18" height="18" viewBox="0 0 24 24" fill="none" stroke="#fff" stroke-width="1.6"><circle cx="12" cy="12" r="9"/><path d="M3 12h18M12 3c3 3 3 15 0 18M12 3c-3 3-3 15 0 18"/></svg>www.veltrasync.example
  </p>
</section>

<section class="card card-back">
  <div class="dna-art" role="img" aria-label="Faint blue illustration of a DNA double helix"></div>
  <ul class="features">
    <li class="feature">
      <svg width="16" height="16" viewBox="0 0 16 16" fill="none" stroke="#1f4f9c" stroke-width="1.4"><circle cx="8" cy="8" r="7"/><path d="M5 8.2l2 2 4-4"/></svg>
      <span class="feature-title">Wide Variety of Sample Types</span>
      IRB-approved samples mimicking crime scene substances, including semen, hair, bone, saliva, blood, and vaginal epithelial cells
    </li>
    <li class="feature">
      <svg width="16" height="16" viewBox="0 0 16 16" fill="none" stroke="#1f4f9c" stroke-width="1.4"><circle cx="8" cy="8" r="7"/><path d="M5 8.2l2 2 4-4"/></svg>
      Diverse Scenarios: Simulate sexual assault and degraded samples for varied conditions.
    </li>
    <li class="feature">
      <svg width="16" height="16" viewBox="0 0 16 16" fill="none" stroke="#1f4f9c" stroke-width="1.4"><circle cx="8" cy="8" r="7"/><path d="M5 8.2l2 2 4-4"/></svg>
      Custom Solutions: Tailored DNA quantities and concentrations to suit your lab’s needs.
    </li>
  </ul>

  <aside class="offer">
    <div class="offer-inner">
      <p class="offer-pct">10%</p>
      <p class="offer-off">OFF</p>
      <p class="offer-label">USE DISCOUNT CODE</p>
      <p class="offer-code">PRAX47</p>
    </div>
  </aside>

  <h2 class="brand-name">VeltraSync</h2>
  <p class="slogan">PRECISION IN EVERY SAMPLE</p>
  <p class="back-contact back-phone">
    <svg width="18" height="18" viewBox="0 0 24 24" fill="none" stroke="#1f4f9c" stroke-width="1.6"><path d="M5 3h4l2 5-2.5 1.5a11 11 0 0 0 6 6L16 13l5 2v4a2 2 0 0 1-2 2A16 16 0 0 1 3 5a2 2 0 0 1 2-2z"/></svg>
    <span>+1 555 014 2876</span>
  </p>
  <p class="back-contact back-web">
    <svg width="18" height="18" viewBox="0 0 24 24" fill="none" stroke="#1f4f9c" stroke-width="1.6"><circle cx="12" cy="12" r="9"/><path d="M3 12h18M12 3c3 3 3 15 0 18M12 3c-3 3-3 15 0 18"/></svg>
    <span>www.<span class="web-name">veltrasync</span>.example</span>
  </p>

  <div class="mail-area mail-area-top"></div>
  <div class="mail-area mail-area-bottom"></div>
</section>

</body>
</html>
```